Stationery Design Project for Marketing Consultancy

I have started a new consultancy business and require the following elements to be designed using existing logo:
• Business card
• Letterhead
• Envelope (DL, C4, C5)
• Microsoft word template for report writing
• A4 Presentation Folder
• Powerpoint template
COPY FOR FRONT AND BACK OF BUSINESS CARD
logo
'Countable Growth. Bold Outcomes' slogan (but no need to use existing lockup with logo)
name, B Bus. Mktg, Grad Dip Digital Mktg, CPM (post nominal abbreviations in smaller font)
mobile: 04XX-XXX-XXX (I will give details to the winner to add)
website: www.quorvale.com.au
email: info@quorvale.com.au
COPY FOR LETTERHEAD
Logo
Company Name
Please, submit your designs that include business card, letterhead and envelope. Once selected the winner will be asked to complete the project by creating the rest of the artwork.
FINAL FILES
Print ready files to be supplied as well as Indesign files so that minor amends can be made if necessary in future.
• Layered vectors in EPS & PDF
• Screen quality JPEG & PNGs
ABOUT THE BUSINESS: QUORVALE
I work with clients to understand their business challenges, developing and executing measurable marketing strategies tied to key business metrics. Services include:
Services include:
• Business planning and business development
• Marketing and brand strategy
• Insight-driven integrated campaigns
• Loyalty programs and retention marketing
• Marketing automation
• Direct marketing (traditional and digital)
• Content strategy and development
Hi everyone,
Target Market(s)
Corporate decision makers (heads of marketing, general managers etc) and small to medium sized business owners. Predominately male aged 35+
Industry/Entity Type
Marketing
Requirements
Must have
- BRAND PERSONALITY
The successful design will communicate brand personality. I am a professional, results-driven entrepreneur, but want to show off my creative flair.
MEMORABILITY
Looking for a unique and eye-catching design. Am considering special printing effects (die cuts, letterpress, interactive elements, embossing, foiling etc) or a striking minimalist approach.
Nice to have
- I have a mission that could be incorporated on reverse if room -
Turning insights into actions & passion into profit.
Should not have
- Use of pink or green.

```html
<!DOCTYPE html>
<html lang="en">
<head>
<meta charset="utf-8">
<title>Quorvale Stationery</title>
<link href="https://fonts.googleapis.com/css2?family=Open+Sans:wght@400;700;800&display=swap" rel="stylesheet">
<style>
  :root {
    --ink: #000000;
    --paper: #ffffff;
    --backdrop: #cfcfd2;
    --mark: #ffffff;
    --muted: #d8d8d8;
  }
  * { margin: 0; padding: 0; box-sizing: border-box; }
  html, body { width: 1200px; height: 1072px; overflow: hidden; }
  body {
    background: var(--backdrop);
    font-family: "Open Sans", Arial, sans-serif;
    position: relative;
  }
  .sheet { position: absolute; background: var(--paper); overflow: hidden; }
  .band { position: absolute; left: 0; right: 0; bottom: 0; background: var(--ink); color: var(--mark); }

  .brand { display: flex; flex-direction: column; align-items: center; color: var(--mark); }
  .brand__dot { border-radius: 50%; background: var(--mark); }
  .brand__name { font-weight: 800; letter-spacing: 0.02em; line-height: 1; }
  .brand__tagline { font-weight: 400; text-transform: uppercase; line-height: 1; color: var(--muted); white-space: nowrap; }

  .contact { position: absolute; color: var(--mark); font-size: 5.5px; line-height: 1.45; }
  .contact__company { font-weight: 700; font-size: 6px; }
  .contact__web { font-weight: 700; }
  .web { position: absolute; color: var(--mark); font-size: 5.5px; font-weight: 700; }

  /* business cards */
  .card { position: absolute; top: 169px; width: 131px; height: 86px; background: var(--ink); }
  .card--front { left: 195px; }
  .card--back { left: 345px; }
  .card--front .brand { position: absolute; left: 0; right: 0; top: 20px; }
  .card--front .brand__dot { width: 20px; height: 20px; margin-bottom: 5px; }
  .card--front .brand__name { font-size: 13px; }
  .card--front .brand__tagline { font-size: 3.6px; margin-top: 2px; }
  .card--back .brand { position: absolute; right: 6px; top: 6px; }
  .card--back .brand__dot { width: 9px; height: 9px; margin-bottom: 2px; }
  .card--back .brand__name { font-size: 5.5px; }
  .card--back .contact { left: 27px; top: 27px; }

  /* DL envelope */
  .dl { left: 603px; top: 114px; width: 385px; height: 181px; }
  .dl .band { height: 37px; }
  .dl .brand { position: absolute; left: 24px; top: 4px; }
  .dl .brand__dot { width: 14px; height: 14px; margin-bottom: 3px; }
  .dl .brand__name { font-size: 8px; }
  .dl .brand__tagline { font-size: 2.4px; margin-top: 1px; }
  .dl .contact { left: 213px; top: 8px; }
  .dl .web { right: 12px; top: 24px; }

  /* letterhead */
  .letterhead { left: 191px; top: 327px; width: 360px; height: 484px; }
  .letterhead .band { height: 46px; }
  .letterhead .brand { position: absolute; left: 18px; top: 8px; }
  .letterhead .brand__dot { width: 14px; height: 14px; margin-bottom: 3px; }
  .letterhead .brand__name { font-size: 8px; }
  .letterhead .brand__tagline { font-size: 2.4px; margin-top: 1px; }
  .letterhead .contact { left: 140px; top: 10px; }
  .letterhead .web { right: 14px; top: 23px; }

  /* C4 envelope */
  .c4 { left: 597px; top: 327px; width: 396px; height: 621px; }
  .c4__flap { position: absolute; left: 0; top: 0; }
  .c4__flap-brand { position: absolute; left: 0; right: 0; top: 16px; }
  .c4 .brand__dot { width: 34px; height: 34px; margin-bottom: 8px; }
  .c4 .brand__name { font-size: 20px; }
  .c4 .brand__tagline { font-size: 5.5px; margin-top: 3px; }
  .c4 .band { height: 77px; }
  .c4 .band .brand { position: absolute; left: 0; right: 0; top: 7px; }
  .c4 .band .brand__dot { width: 30px; height: 30px; margin-bottom: 6px; }
  .c4 .band .brand__name { font-size: 15px; }
  .c4 .band .brand__tagline { font-size: 4px; margin-top: 2px; }
</style>
</head>
<body>

  <section class="card card--front" aria-label="Business card front">
    <div class="brand">
      <span class="brand__dot"></span>
      <span class="brand__name">QUORVALE</span>
      <span class="brand__tagline">Countable Growth. Bold Outcomes</span>
    </div>
  </section>

  <section class="card card--back" aria-label="Business card back">
    <div class="brand">
      <span class="brand__dot"></span>
      <span class="brand__name">QUORVALE</span>
    </div>
    <div class="contact">
      <div class="contact__company">Company Name</div>
      <div>M: xxx xxx xxxx</div>
      <div>E: info@quorvale.com.au</div>
      <div class="contact__web">www.quorvale.com.au</div>
    </div>
  </section>

  <section class="sheet dl" aria-label="DL envelope">
    <div class="band">
      <div class="brand">
        <span class="brand__dot"></span>
        <span class="brand__name">QUORVALE</span>
        <span class="brand__tagline">Countable Growth. Bold Outcomes</span>
      </div>
      <div class="contact">
        <div class="contact__company">Company Name</div>
        <div>M: xxx xxx xxxx</div>
        <div>E: info@quorvale.com.au</div>
      </div>
      <div class="web">www.quorvale.com.au</div>
    </div>
  </section>

  <section class="sheet letterhead" aria-label="Letterhead">
    <div class="band">
      <div class="brand">
        <span class="brand__dot"></span>
        <span class="brand__name">QUORVALE</span>
        <span class="brand__tagline">Countable Growth. Bold Outcomes</span>
      </div>
      <div class="contact">
        <div class="contact__company">Company Name</div>
        <div>M: xxx xxx xxxx</div>
        <div>E: info@quorvale.com.au</div>
      </div>
      <div class="web">www.quorvale.com.au</div>
    </div>
  </section>

  <section class="sheet c4" aria-label="C4 envelope">
    <svg class="c4__flap" width="396" height="114" viewBox="0 0 396 114" aria-hidden="true">
      <path d="M0 0 H396 V78 A36 36 0 0 0 360 114 H36 A36 36 0 0 0 0 78 Z" fill="var(--ink)"/>
    </svg>
    <div class="brand c4__flap-brand">
      <span class="brand__dot"></span>
      <span class="brand__name">QUORVALE</span>
      <span class="brand__tagline">Countable Growth. Bold Outcomes</span>
    </div>
    <div class="band">
      <div class="brand">
        <span class="brand__dot"></span>
        <span class="brand__name">QUORVALE</span>
        <span class="brand__tagline">Countable Growth. Bold Outcomes</span>
      </div>
    </div>
  </section>

</body>
</html>
```